Rioja winery needs a new label design

A family-owned winery in Spain's Rioja Oriental region is looking to create a new label for a wine named "Dorvi" Arabic for Castle, that reflects the land from which the wine is born. From the remote village of Quel, La Rioja Oriental, with the backdrop of the Sierra Yerga mountains and the Barrio de Bodegas, or group of caves where locals have produced wines for centuries. Wine name:
2018 Dorvi Rioja Tempranillo
Quel, Rioja Oriental
Spain

Font styles to use
Serif
Sans Serif
Decorative
Script

Requirements
Must have
• vines, vineyards, grapes
Nice to have
• mountains,
Should not have
• castles. we already have a label design with the castle

```html
<!DOCTYPE html>
<html lang="en">
<head>
<meta charset="utf-8">
<title>Dorvi Rioja Tempranillo 2018 – Label</title>
<link href="https://fonts.googleapis.com/css2?family=Vollkorn:wght@600&family=Raleway:wght@400;700&display=swap" rel="stylesheet">
<style>
  :root {
    --wine: #a1385a;
    --frame-grey: #999999;
    --text-grey: #8a8083;
    --paper: #ffffff;
    --art-light: #d9d9d9;
    --art-mid: #8f8f8f;
    --art-dark: #5a5c5c;
  }
  * { margin: 0; padding: 0; box-sizing: border-box; }
  html, body { width: 1052px; height: 1200px; overflow: hidden; background: var(--paper); }
  .label { position: relative; width: 1052px; height: 1200px; background: var(--paper); }
  .label-frame { position: absolute; inset: 0; }
  .wine-name {
    position: absolute; left: 0; right: 0; top: 268px;
    text-align: center;
    font-family: "Vollkorn", Georgia, serif; font-weight: 600;
    font-size: 124px; line-height: 1; letter-spacing: 2px;
    color: var(--wine);
  }
  .landscape-art {
    position: absolute; left: 261px; top: 441px; width: 495px; height: 336px;
    border-radius: 26px;
    background: linear-gradient(180deg, #ffffff 0%, #f2f2f2 18%, var(--art-light) 42%, var(--art-mid) 72%, var(--art-dark) 100%);
  }
  .varietal, .vintage {
    position: absolute; left: 0; right: 0; text-align: center;
    font-family: "Raleway", Arial, sans-serif; font-weight: 700;
    color: var(--text-grey); line-height: 1;
  }
  .varietal { top: 805px; font-size: 44px; }
  .vintage { top: 850px; font-size: 50px; }
  .origin {
    position: absolute; left: 0; right: 0; top: 949px; text-align: center;
    font-family: "Raleway", Arial, sans-serif; font-weight: 400;
    font-size: 32px; line-height: 1; color: var(--wine);
    white-space: pre;
  }
</style>
</head>
<body>
<main class="label">
  <svg class="label-frame" width="1052" height="1200" viewBox="0 0 1052 1200">
    <polygon class="frame-outer" points="234,133 780,133 908,248 908,974 792,1090 226,1090 108,974 108,251"
             fill="none" stroke="var(--wine)" stroke-width="6"/>
    <polygon class="frame-inner" points="238,143 775,143 897,254 897,968 786,1080 231,1080 119,969 119,255"
             fill="none" stroke="var(--frame-grey)" stroke-width="2.5"/>
  </svg>

  <h1 class="wine-name">DORVI</h1>

  <div class="landscape-art" role="img"
       aria-label="Grey-toned illustration of vine leaves and a bunch of grapes over the rocky Sierra Yerga mountains with pine trees"></div>

  <p class="varietal">Rioja Tempranillo</p>
  <p class="vintage">2018</p>
  <p class="origin">Quel, Rioja Oriental  Spain</p>
</main>
</body>
</html>
```